Direct to Consumer extended service contract business with a new disruptive business model needs a

We need a customized wordpress design for a company called 'Tall Harbor Assurance'.
We provide an innovative and unique service contract protection program direct to consumers. This program provides monthly coverage for all electronics purchased in the last 4 years and all electronics the consumer purchases in the future for a low monthly fee. The overall design should communicate a sense of legitimacy, ethics, and superior customer service and support (in an industry that has a huge PR issue to overcome).
Electronics is the first product group, other product groups with different price points to launch in the future..

Target Market(s)

All purchasers of electronic goods...all demographics

Industry/Entity Type

Electronics

Font styles to use
Sans Serif

Requirements
Must have
• Customer Testimonials
Industry News
Customer ratings
Blog posts
Call to action messaging
Like the functional elements and design of bramblequill.example (need to be better)
Nice to have
• Like to see video testimonials
Social network "whats trending related to electronics or service contract industry"
Easy way to register products for warranty

```html
<!DOCTYPE html>
<html lang="en">
<head>
<meta charset="utf-8">
<title>Become a Member – Tall Harbor Assurance</title>
<link rel="stylesheet" href="https://fonts.googleapis.com/css2?family=Montserrat:wght@600;700;800&family=Lato:wght@400&family=Quicksand:wght@300;400&display=swap">
<style>
  :root {
    --coral: #f44f41;
    --ink: #1f1f1f;
    --white: #ffffff;
    --page: #ffffff;
  }
  * { box-sizing: border-box; margin: 0; padding: 0; }
  html, body {
    width: 1200px;
    height: 633px;
    overflow: hidden;
    background: var(--page);
  }
  .membership {
    position: relative;
    width: 1200px;
    height: 633px;
  }
  .membership__title {
    position: absolute;
    top: 52px;
    left: 0;
    width: 100%;
    text-align: center;
    font-family: "Montserrat", sans-serif;
    font-weight: 800;
    font-size: 33px;
    letter-spacing: -0.5px;
    color: var(--ink);
  }
  .membership__divider {
    position: absolute;
    top: 100px;
    left: 465px;
    width: 257px;
    height: 12px;
  }
  .membership__intro {
    position: absolute;
    top: 129px;
    left: 0;
    width: 100%;
    text-align: center;
    font-family: "Lato", sans-serif;
    font-size: 15.5px;
    color: var(--ink);
  }
  .plan {
    position: absolute;
    top: 186px;
    width: 270px;
    height: 405px;
    background: var(--coral);
    padding: 4px;
  }
  .plan--electronics { left: 108px; }
  .plan--automotive { left: 460px; }
  .plan--appliance { left: 821px; }
  .plan__frame {
    width: 100%;
    height: 100%;
    border: 1px solid var(--white);
    display: flex;
    flex-direction: column;
    align-items: center;
    justify-content: center;
    padding-bottom: 16px;
    color: var(--white);
    text-align: center;
  }
  .plan__icon { display: block; margin-bottom: 10px; }
  .plan__name {
    font-family: "Montserrat", sans-serif;
    font-weight: 700;
    font-size: 15.5px;
    line-height: 24px;
    width: 240px;
  }
  .plan__price {
    font-family: "Quicksand", sans-serif;
    font-weight: 300;
    font-size: 31px;
    margin-top: 10px;
  }
  .plan__fee {
    font-family: "Quicksand", sans-serif;
    font-weight: 400;
    font-size: 18px;
    margin-top: 18px;
  }
  .plan__status {
    font-family: "Quicksand", sans-serif;
    font-weight: 400;
    font-size: 19px;
    margin-top: 18px;
  }
</style>
</head>
<body>
<section class="membership">
  <h1 class="membership__title">BECOME A MEMBER</h1>
  <svg class="membership__divider" viewBox="0 0 257 12" aria-hidden="true">
    <g stroke="#f44f41" stroke-width="2.2" fill="none">
      <line x1="0" y1="6" x2="52" y2="6"/>
      <line x1="82" y1="6" x2="175" y2="6"/>
      <line x1="205" y1="6" x2="257" y2="6"/>
      <path d="M56 11 L60 1 M62 11 L66 1 M68 11 L72 1 M74 11 L78 1"/>
      <path d="M179 1 L183 11 M185 1 L189 11 M191 1 L195 11 M197 1 L201 11"/>
    </g>
  </svg>
  <p class="membership__intro">Join the Tall Harbor Assurance Network and never buy an in-store Service Contract again.</p>

  <article class="plan plan--electronics">
    <div class="plan__frame">
      <svg class="plan__icon" width="52" height="52" viewBox="0 0 52 52" fill="none" stroke="#fff" stroke-width="1.6" aria-hidden="true">
        <rect x="18" y="1" width="20" height="14" rx="1"/>
        <line x1="28" y1="15" x2="28" y2="19"/>
        <line x1="22" y1="19" x2="34" y2="19"/>
        <rect x="1" y="21" width="50" height="4"/>
        <rect x="3" y="25" width="16" height="26"/>
        <line x1="3" y1="33" x2="19" y2="33"/>
        <line x1="3" y1="42" x2="19" y2="42"/>
        <line x1="9" y1="29" x2="13" y2="29"/>
        <line x1="9" y1="37" x2="13" y2="37"/>
        <line x1="9" y1="46" x2="13" y2="46"/>
        <line x1="45" y1="25" x2="45" y2="51"/>
        <line x1="49" y1="25" x2="49" y2="51"/>
      </svg>
      <h2 class="plan__name">ELECTRONICS PROTECTION PLAN</h2>
      <p class="plan__price">$19.95/month</p>
      <p class="plan__fee">+ $29.95/Signup fee</p>
    </div>
  </article>

  <article class="plan plan--automotive">
    <div class="plan__frame">
      <svg class="plan__icon" width="44" height="38" viewBox="0 0 44 38" fill="none" stroke="#fff" stroke-width="1.6" aria-hidden="true">
        <path d="M8 35 A19 19 0 1 1 36 35"/>
        <line x1="22" y1="5" x2="22" y2="9"/>
        <line x1="8" y1="11" x2="10.5" y2="13.5"/>
        <line x1="36" y1="11" x2="33.5" y2="13.5"/>
        <line x1="3" y1="24" x2="7" y2="24"/>
        <line x1="41" y1="24" x2="37" y2="24"/>
        <line x1="22" y1="24" x2="30" y2="30" stroke-width="2.4"/>
        <circle cx="22" cy="24" r="2" fill="#fff"/>
      </svg>
      <h2 class="plan__name">AUTOMOTIVE PROTECTION PLAN</h2>
      <p class="plan__status">Coming Soon</p>
    </div>
  </article>

  <article class="plan plan--appliance">
    <div class="plan__frame">
      <svg class="plan__icon" width="52" height="54" viewBox="0 0 52 54" fill="none" stroke="#fff" stroke-width="1.6" aria-hidden="true">
        <line x1="26" y1="1" x2="26" y2="6"/>
        <line x1="10" y1="8" x2="13.5" y2="11.5"/>
        <line x1="42" y1="8" x2="38.5" y2="11.5"/>
        <line x1="2" y1="23" x2="7" y2="23"/>
        <line x1="50" y1="23" x2="45" y2="23"/>
        <line x1="10" y1="38" x2="13.5" y2="34.5"/>
        <line x1="42" y1="38" x2="38.5" y2="34.5"/>
        <path d="M19 40 C19 34 12 31 12 23 A14 14 0 0 1 40 23 C40 31 33 34 33 40 Z"/>
        <path d="M22 40 L22 30 M30 40 L30 30"/>
        <circle cx="22" cy="28" r="2.5"/>
        <circle cx="30" cy="28" r="2.5"/>
        <line x1="19" y1="44" x2="33" y2="44"/>
        <line x1="19" y1="48" x2="33" y2="48"/>
        <line x1="22" y1="52" x2="30" y2="52"/>
      </svg>
      <h2 class="plan__name">APPLIANCE PROTECTION PLAN</h2>
      <p class="plan__status">Coming Soon</p>
    </div>
  </article>
</section>
</body>
</html>
```